Event Center Website

We need a new website design for an upscale event center in Reno, Nevada. The building hosts everything from weddings to corporate events to funerals and it competitively more expensive. The overall look and feel is consistent with a Lake Tahoe aesthetic. The current site can be viewed at www.thefernlodgeva.com. They are looking for a major upgrade. A sample site they like is www.quillmarshlodge.com. We have new photography available (some attached). The site should be very visual. A site map is attached as well for direction on what elements the site should include as well as labels for navigation. I am looking for a home page and sample interior page. Any questions, let me know. Thanks.
Updates

I have added some photography of the center itself for use rather than stock photography. Thanks!

Target Market(s)

Brides, professionals, high-income

Industry/Entity Type

Building

Requirements
Must have
• See site map

```html
<!DOCTYPE html>
<html lang="en">
<head>
<meta charset="utf-8">
<title>Fern Lodge – About Us</title>
<link href="https://fonts.googleapis.com/css2?family=Ubuntu:wght@400;500&display=swap" rel="stylesheet">
<style>
:root{
  --brown-dark:#4a2812;
  --brown:#7a3e08;
  --orange:#c96f1d;
  --cream:#f5e6c4;
  --cream-panel:rgba(243,226,190,.88);
  --text:#2b1a0c;
  --quote:#5a3a1c;
  --name:#a8611a;
  --arrow:#8a4420;
}
*{box-sizing:border-box;margin:0;padding:0}
html,body{width:1200px;height:874px;overflow:hidden}
body{position:relative;background:var(--cream);font-family:'Ubuntu',sans-serif;color:var(--text)}
.hero{position:absolute;left:0;top:0;width:1200px;height:708px;
  background:radial-gradient(ellipse at 50% 35%,#f2c46a 0%,#b9772c 30%,#5c3414 60%,#3a2a22 100%)}
.hero-bottom{position:absolute;left:0;top:520px;width:1200px;height:188px;background:linear-gradient(180deg,rgba(60,50,50,0),#4a4344)}
.top-links{position:absolute;left:849px;top:0;width:227px;height:52px;background:var(--brown-dark);
  display:flex;align-items:center;justify-content:center;gap:22px;color:#f3e4cc;font-size:15px}
.top-links .sep{width:2px;height:26px;background:#f3e4cc}
.nav{position:absolute;left:98px;top:52px;width:1005px;height:58px;background:var(--cream);display:flex;align-items:center}
.brand{width:224px;display:flex;align-items:center;justify-content:center;gap:8px;font-size:24px;color:var(--brown-dark);font-weight:500}
.brand .dot{width:10px;height:10px;border-radius:50%;background:var(--brown-dark)}
.nav a{font-size:14.5px;color:var(--text);text-decoration:none;font-weight:500;padding:0 17px;line-height:58px}
.nav a.active{background:var(--brown);color:#f5e3c3;padding:0 14px}
.panel{position:absolute;left:99px;top:259px;width:1004px;height:427px;background:var(--cream-panel)}
.panel h1{position:absolute;left:28px;top:30px;font-size:17px;font-weight:500;padding-bottom:6px;border-bottom:1px solid #8a6a4a}
.intro{position:absolute;left:36px;top:76px;width:940px;font-size:14.5px;line-height:25px}
.portrait{position:absolute;left:38px;top:165px;width:198px;height:198px;background:linear-gradient(135deg,#9a5a15,#c27b2a 60%,#8a4c10)}
.quote{position:absolute;left:242px;top:181px;width:710px;text-align:center;font-size:15px;line-height:27.5px;color:var(--quote)}
.author{position:absolute;left:470px;top:281px;width:215px;text-align:center;font-size:17px;color:var(--name);display:flex;justify-content:center;align-items:center;gap:6px}
.dots{position:absolute;left:544px;top:378px;display:flex;gap:8px}
.dots span{width:10px;height:10px;background:var(--brown)}
.arrow{position:absolute;top:385px;width:48px;height:48px;border-radius:50%;background:var(--arrow)}
.arrow.prev{left:21px}.arrow.next{left:1128px}
.arrow svg{display:block}
.subscribe{position:absolute;left:131px;top:747px;width:339px;height:60px;background:var(--brown);display:flex;align-items:center;color:#f5e3c3}
.subscribe .field{flex:1;padding-left:9px;font-size:14.5px;display:flex;align-items:center;justify-content:space-between;padding-right:10px}
.subscribe .send{width:55px;height:60px;background:var(--orange);border-radius:0 4px 4px 0;display:flex;align-items:center;justify-content:center;font-size:14.5px}
.contact{position:absolute;left:495px;top:748px;width:362px;height:58px;background:var(--brown-dark);border-radius:3px;display:flex;color:#f3e4cc;font-size:13px;line-height:24px}
.contact .addr{width:150px;padding:6px 0 0 11px;border-right:1px solid #7a5030}
.contact .reach{padding:6px 0 0 9px}
.contact .label{color:var(--orange)}
.social{position:absolute;left:887px;top:748px;width:189px;height:59px;background:var(--brown-dark);border-radius:3px;display:flex;align-items:center;gap:11px;padding-left:20px}
.social span{width:29px;height:29px;background:#c9a77c}
.footer-nav{position:absolute;left:0;top:834px;width:1200px;display:flex;justify-content:center;gap:28px;font-size:13.5px;color:var(--brown-dark)}
</style>
</head>
<body>
<div class="hero" role="img" aria-label="Interior of the event hall with chandelier, draped ceiling fabric and rows of white chairs"></div>
<div class="hero-bottom"></div>

<div class="top-links"><span>FAQ</span><span class="sep"></span><span>TESTIMONIAL</span></div>

<nav class="nav">
  <div class="brand"><span class="dot"></span>Fern Lodge</div>
  <a class="active">ABOUT US</a><a>GALLERY</a><a>WEDDING</a><a>MEETINGS</a><a>OTHER EVENTS</a><a>CATERING</a><a>MENUS</a>
</nav>

<div class="arrow prev"><svg width="48" height="48"><path d="M27 17l-7 7 7 7M33 17l-7 7 7 7" fill="none" stroke="#fff" stroke-width="2"/></svg></div>
<div class="arrow next"><svg width="48" height="48"><path d="M15 17l7 7-7 7M21 17l7 7-7 7" fill="none" stroke="#fff" stroke-width="2"/></svg></div>

<section class="panel">
  <h1>ABOUT US</h1>
  <p class="intro">The staff at The Fern Lodge is experienced, talented, and committed to creating a carefree and expertly organized event.&nbsp; Our seasoned staff will assist you in planning and coordinating a successful event with gourmet catering anda full service bar.</p>
  <div class="portrait" role="img" aria-label="Portrait photo of a smiling guest in a suit"></div>
  <p class="quote">“The Fern Lodge is such a beautiful venue, that I was immediately attracted to it as soon as I walked<br>through the doors. Since I have been here I can see how the beauty of the space in combination<br>with our inviting food creates lasting memories for our guests.”</p>
  <div class="author">Marla <svg width="20" height="20"><path d="M3 17l1-5 10-10 4 4-10 10z" fill="#c96f1d"/></svg></div>
  <div class="dots"><span></span><span></span><span></span><span></span></div>
</section>

<div class="subscribe">
  <div class="field">ENTER YOUR EMAIL
    <svg width="32" height="30"><path d="M2 12l14-10 14 10v16H2z" fill="#fff"/><path d="M2 12l14 10 14-10" fill="none" stroke="#7a3e08" stroke-width="1.5"/><text x="11" y="14" font-size="10" fill="#7a3e08" font-family="Ubuntu,sans-serif">@</text></svg>
  </div>
  <div class="send">SEND</div>
</div>

<div class="contact">
  <div class="addr">48 Ridgecrest Lane<br>Reno, NV 89519</div>
  <div class="reach"><span class="label">Phone:</span>&nbsp; 775-555-0142<br><span class="label">Email:</span>&nbsp; info@thefernlodgeva.com</div>
</div>

<div class="social"><span></span><span></span><span></span><span></span></div>

<div class="footer-nav"><span>ABOUT US</span><span>GALLERY</span><span>WEDDING</span><span>MEETINGS</span><span>OTHER EVENTS</span><span>CATERING</span><span>MENUS</span></div>
</body>
</html>
```